Menu board for car wash

I need to have a menu board designed for my car wash. I would like for it to replicate the attached graphics of other menu boards other car washes are using. The menu board will be printed locally and be cut out with a router. I want the menu board to clearly show what they are buying and promote buying the top wash package. I also want "the Fullset" package to show that you can buy a monthly plan for $23.95 and receive this wash unlimited times per month. I have attached my menu that i have now (Hendleybrightmenu). I would like for this new menu to have the same wording as the previous menu for the wash packages. The only addition is a new wash package "Summit Glow" which is now the top wash package. The new menu i would like to have going vertical and I would like my logo on the top. This menu would be 8' high and 4'wide.

Target Market(s)

Looking to have this menu be attractive and inviting. The top package should stand out the most and the lowest package should barely be noticeable ( basic wash)
I am targeting customer from the ages of 16-65 years old.

Industry/Entity Type

Automotive

Font styles to use
Serif
Sans Serif
Decorative
Other font styles liked:
• any font that flows with the design

Colors

Designer to choose colors to be used in the design.

Requirements
Must have
• This menu will be die cut out. It must fit in a 8' x 4' vertical art board.
• The wash packages will need to go from top to bottom
• They should be listed as follows
• Summit Glow $18
• The Fullset $13 ( also add Unlimited for $23.95)
• Deluxe $10
• Basic $8
• I would like to have an extras section also added just like my original menu. This can be at the bottom of the menu If you have any cool graphics that go with my theme or washes please feel free.
• The new Summit Glow wash will have the following included:
• Presoak
• Bug Treatment
• wheel cleaner
• Undercarriage wash
• Triple Foam Polish
• Clear Coat Protectant
• Hot Wax Treatment ( you can use graphic that is on my old menu for this item)
• Tire Shine ( You can use the Silk Comet logo)
• Hand Towel Dried
Nice to have
• Incorporate my business hours also on the menu
• the hours are:
• Monday-Saturday 8:00 Am-6:00 Pm
• Sunday 8:00 Am-5:00 Pm
• Weather may effect these hours
Should not have
• Text should be clearly visable so anyone car read it easily

```html
<!DOCTYPE html>
<html lang="en">
<head>
<meta charset="utf-8">
<title>Hendley's Bright Car Wash – Menu Board</title>
<link rel="stylesheet" href="https://fonts.googleapis.com/css2?family=Archivo+Black&family=Roboto+Condensed:wght@600;700&family=Montserrat:wght@700;800&display=swap">
<style>
  :root{
    --page:#e9eaeb;
    --board:#ffffff;
    --red:#d7141f;
    --red-dark:#7d0a10;
    --red-deep:#5e070c;
    --yellow:#f6d21a;
    --yellow-deep:#f2b705;
    --blue:#1b3d8f;
    --blue-dark:#101f55;
    --ink:#111111;
    --white:#ffffff;
    --silver-1:#f1f1f1;
    --silver-2:#9c9c9c;
    --silver-3:#3a3a3a;
  }
  *{margin:0;padding:0;box-sizing:border-box}
  html,body{width:1200px;height:2179px;overflow:hidden;background:var(--page)}
  .canvas{position:relative;width:1200px;height:2179px}
  .board{position:absolute;left:128px;top:142px;width:959px;height:1968px;background:var(--board);box-shadow:4px 6px 10px rgba(0,0,0,.35)}

  .logo-frame{position:absolute;left:126px;top:142px;width:963px;height:338px;background:var(--red);border-radius:60px 60px 40px 40px;padding:14px;z-index:3}
  .logo-panel{width:100%;height:100%;background:var(--yellow);border-radius:48px 48px 30px 30px;display:flex;flex-direction:column;align-items:center;justify-content:center;color:var(--red);font-family:"Archivo Black",sans-serif;text-align:center;line-height:1}
  .logo-name{font-size:74px}
  .logo-sub{font-size:118px;margin-top:6px}

  .band{position:absolute;left:128px;width:959px;background:linear-gradient(90deg,var(--silver-1) 0%,#d4d4d4 30%,#ffffff 55%,var(--silver-2) 85%,var(--silver-3) 100%);box-shadow:0 4px 8px rgba(0,0,0,.45);z-index:2}
  .band-icon{position:absolute;background:var(--red);border-radius:14px}
  .band-title{position:absolute;font-family:"Archivo Black",sans-serif;color:var(--ink);letter-spacing:2px;white-space:nowrap}
  .band--top{top:443px;height:167px}
  .band--mid{top:959px;height:142px}
  .band--low{top:1479px;height:145px}

  .panel{position:absolute;left:128px;width:959px;overflow:hidden}
  .panel--red{top:610px;height:349px;background:radial-gradient(ellipse at 60% 60%,#e3232c 0%,#b30f18 55%,var(--red-dark) 100%)}
  .panel--blue{top:1101px;height:378px;background:radial-gradient(ellipse at 40% 35%,#2552b5 0%,var(--blue) 45%,var(--blue-dark) 100%)}
  .panel--yellow{top:1624px;height:425px;background:linear-gradient(180deg,var(--yellow-deep) 0%,var(--yellow) 45%,#fbe34a 100%)}

  .list{position:absolute;list-style:none;font-family:"Roboto Condensed",sans-serif;font-weight:700;color:var(--white);text-transform:uppercase}
  .list li{position:absolute;left:0;white-space:nowrap;display:flex;align-items:flex-start}
  .list svg{flex:none}
  .list--lg{font-size:36px;line-height:1}
  .list--lg svg{width:28px;height:28px;margin:4px 12px 0 0}
  .list--sm{font-size:26px;line-height:1;color:var(--ink)}
  .list--sm svg{width:20px;height:20px;margin:3px 9px 0 0}

  .badge{position:absolute;overflow:visible}
  .badge text{font-family:"Roboto Condensed",sans-serif;font-weight:700}

  .brand-chip{position:absolute;font-family:"Roboto Condensed",sans-serif;font-weight:700;text-transform:uppercase;text-align:center;white-space:nowrap}
  .brand-comet{left:652px;top:1156px;width:190px;font-size:36px;color:var(--white)}
  .brand-shield{left:660px;top:1240px;width:190px;height:54px;background:var(--yellow);color:var(--blue-dark);font-size:34px;line-height:54px}

  .unlimited{position:absolute;left:613px;top:1361px;width:455px;height:63px;border-radius:32px;background:var(--red);color:var(--white);font-family:"Montserrat",sans-serif;font-weight:700;font-size:30px;display:flex;align-items:center;justify-content:center}
  .unlimited strong{font-weight:800;font-size:36px;margin-left:10px}

  .wash-mark{position:absolute;left:628px;top:1788px;width:280px;text-align:center;font-family:"Archivo Black",sans-serif;font-size:46px;color:var(--red)}

  .footer-wave{position:absolute;left:128px;top:1850px;width:959px;height:199px}
  .hours-title{position:absolute;left:164px;top:1944px;font-family:"Roboto Condensed",sans-serif;font-weight:700;font-size:52px;line-height:1;color:var(--white);letter-spacing:1px}
  .hours-note{position:absolute;left:166px;top:2004px;font-family:"Montserrat",sans-serif;font-weight:700;font-size:17px;color:var(--yellow);letter-spacing:1px}
  .hours-list{position:absolute;left:639px;top:1934px;font-family:"Montserrat",sans-serif;font-weight:700;font-size:24px;line-height:34px;color:var(--white);letter-spacing:2px}

  .extras{position:absolute;left:128px;top:2049px;width:959px;height:61px;background:var(--red-deep);display:flex;align-items:center;padding-left:36px;gap:24px;white-space:nowrap}
  .extras-title{font-family:"Archivo Black",sans-serif;font-size:28px;color:var(--yellow);letter-spacing:2px}
  .extras-items{font-family:"Roboto Condensed",sans-serif;font-weight:700;font-size:27px;color:var(--white);text-transform:uppercase;letter-spacing:1px}
</style>
</head>
<body>
<svg width="0" height="0" style="position:absolute">
  <defs>
    <symbol id="tick-box" viewBox="0 0 24 24">
      <rect x="2" y="4" width="17" height="17" rx="3" fill="none" stroke="currentColor" stroke-width="2.6"/>
      <path d="M6 12 l4 4 L22 3" fill="none" stroke="currentColor" stroke-width="3" stroke-linecap="round" stroke-linejoin="round"/>
    </symbol>
    <radialGradient id="gold" cx="45%" cy="40%" r="65%">
      <stop offset="0" stop-color="#fff36a"/>
      <stop offset=".6" stop-color="#f7cc0e"/>
      <stop offset="1" stop-color="#e9a400"/>
    </radialGradient>
    <radialGradient id="coal" cx="45%" cy="40%" r="65%">
      <stop offset="0" stop-color="#3a3a3a"/>
      <stop offset="1" stop-color="#0c0c0c"/>
    </radialGradient>
  </defs>
</svg>

<main class="canvas">
  <div class="board"></div>

  <header class="logo-frame">
    <div class="logo-panel">
      <span class="logo-name">Hendley's Bright</span>
      <span class="logo-sub">Car Wash</span>
    </div>
  </header>

  <!-- Summit Glow -->
  <section class="band band--top">
    <div class="band-icon" role="img" aria-label="Car with bubbles icon" style="left:22px;top:42px;width:106px;height:76px"></div>
    <h2 class="band-title" style="left:212px;top:50px;font-size:60px">SUMMIT GLOW</h2>
  </section>
  <section class="panel panel--red">
    <ul class="list list--lg" style="left:29px;top:35px">
      <li style="top:0"><svg><use href="#tick-box"/></svg>Presoak</li>
      <li style="top:49px"><svg><use href="#tick-box"/></svg>Bug Treatment</li>
      <li style="top:97px"><svg><use href="#tick-box"/></svg>Wheel Cleaner</li>
      <li style="top:146px"><svg><use href="#tick-box"/></svg>Undercarriage Wash</li>
      <li style="top:194px"><svg><use href="#tick-box"/></svg>Triple Foam Polish</li>
    </ul>
    <ul class="list list--lg" style="left:485px;top:35px">
      <li style="top:0"><svg><use href="#tick-box"/></svg>Clear Coat Protectant</li>
      <li style="top:49px"><svg><use href="#tick-box"/></svg>Hot Wax Treatment</li>
      <li style="top:97px"><svg><use href="#tick-box"/></svg>Tire Shine</li>
      <li style="top:146px;line-height:48px;margin-top:-6px"><svg style="margin-top:10px"><use href="#tick-box"/></svg>Hand Towel<br>Dried</li>
    </ul>
    <svg class="badge" style="left:767px;top:145px" width="172" height="172" viewBox="0 0 172 172">
      <circle cx="86" cy="86" r="80" fill="#fff" stroke="#fff" stroke-width="10" stroke-dasharray="0 13.5" stroke-linecap="round"/>
      <circle cx="86" cy="86" r="68" fill="url(#gold)"/>
      <text x="86" y="108" text-anchor="middle" font-size="66" fill="#111"><tspan font-size="40" dy="-14">$</tspan><tspan dy="14">18</tspan></text>
    </svg>
  </section>

  <!-- The Fullset -->
  <section class="band band--mid">
    <div class="band-icon" role="img" aria-label="Tire with sponge icon" style="left:32px;top:30px;width:110px;height:84px;border-radius:42px"></div>
    <h2 class="band-title" style="left:217px;top:38px;font-size:58px">THE FULLSET</h2>
  </section>
  <section class="panel panel--blue">
    <ul class="list list--lg" style="left:29px;top:32px">
      <li style="top:0"><svg><use href="#tick-box"/></svg>Presoak</li>
      <li style="top:50px"><svg><use href="#tick-box"/></svg>Wheel Cleaner</li>
      <li style="top:98px"><svg><use href="#tick-box"/></svg>Undercarriage Wash</li>
      <li style="top:151px"><svg><use href="#tick-box"/></svg>Triple Foam Polish</li>
      <li style="top:202px"><svg><use href="#tick-box"/></svg>Clear Coat</li>
      <li style="top:250px"><svg><use href="#tick-box"/></svg>Hand Towel Dry</li>
    </ul>
    <svg class="badge" style="left:762px;top:33px" width="172" height="172" viewBox="0 0 172 172">
      <circle cx="86" cy="86" r="80" fill="#fff" stroke="#fff" stroke-width="10" stroke-dasharray="0 13.5" stroke-linecap="round"/>
      <circle cx="86" cy="86" r="68" fill="url(#gold)"/>
      <text x="86" y="108" text-anchor="middle" font-size="66" fill="#111"><tspan font-size="40" dy="-14">$</tspan><tspan dy="14">13</tspan></text>
    </svg>
  </section>
  <span class="brand-chip brand-comet">Silk Comet</span>
  <span class="brand-chip brand-shield">Dropshield</span>
  <div class="unlimited">UNLIMITED FOR <strong>$23.95</strong></div>

  <!-- Deluxe & Basic -->
  <section class="band band--low">
    <div class="band-icon" role="img" aria-label="Polisher and car icon" style="left:40px;top:26px;width:88px;height:94px"></div>
    <h2 class="band-title" style="left:162px;top:40px;font-size:58px">DELUXE</h2>
    <div class="band-icon" role="img" aria-label="Car under shower icon" style="left:526px;top:26px;width:84px;height:94px"></div>
    <h2 class="band-title" style="left:627px;top:40px;font-size:58px">BASIC</h2>
  </section>
  <section class="panel panel--yellow">
    <ul class="list list--sm" style="left:35px;top:29px">
      <li style="top:0"><svg><use href="#tick-box"/></svg>Presoak</li>
      <li style="top:35px"><svg><use href="#tick-box"/></svg>Wheel Cleaner</li>
      <li style="top:70px"><svg><use href="#tick-box"/></svg>Undercarriage Wash</li>
      <li style="top:109px"><svg><use href="#tick-box"/></svg>Triple Foam Polish</li>
      <li style="top:144px"><svg><use href="#tick-box"/></svg>Clear Coat</li>
      <li style="top:180px"><svg><use href="#tick-box"/></svg>Hand Towel Dry</li>
    </ul>
    <ul class="list list--sm" style="left:519px;top:29px">
      <li style="top:0"><svg><use href="#tick-box"/></svg>Presoak</li>
      <li style="top:35px"><svg><use href="#tick-box"/></svg>Wash</li>
      <li style="top:70px"><svg><use href="#tick-box"/></svg>Dry</li>
    </ul>
  </section>

  <svg class="footer-wave" viewBox="0 0 959 199" preserveAspectRatio="none" aria-hidden="true">
    <defs>
      <linearGradient id="footer-red" x1="0" y1="0" x2="1" y2="0">
        <stop offset="0" stop-color="#c8121c"/>
        <stop offset="1" stop-color="#8a0b12"/>
      </linearGradient>
    </defs>
    <path d="M0 40 C200 10 420 10 620 30 C760 44 880 30 959 0 L959 199 L0 199 Z" fill="#ffffff"/>
    <path d="M0 52 C200 22 420 22 620 42 C760 56 880 42 959 12 L959 199 L0 199 Z" fill="url(#footer-red)"/>
  </svg>

  <span class="wash-mark">Hendley's</span>

  <svg class="badge" style="left:453px;top:1736px" width="140" height="140" viewBox="0 0 140 140">
    <circle cx="70" cy="70" r="64" fill="#fff" stroke="#fff" stroke-width="8" stroke-dasharray="0 11.2" stroke-linecap="round"/>
    <circle cx="70" cy="70" r="54" fill="url(#coal)"/>
    <text x="70" y="88" text-anchor="middle" font-size="52" fill="#fff"><tspan font-size="32" dy="-10">$</tspan><tspan dy="10">10</tspan></text>
  </svg>
  <svg class="badge" style="left:930px;top:1746px" width="140" height="140" viewBox="0 0 140 140">
    <circle cx="70" cy="70" r="64" fill="#fff" stroke="#fff" stroke-width="8" stroke-dasharray="0 11.2" stroke-linecap="round"/>
    <circle cx="70" cy="70" r="54" fill="url(#coal)"/>
    <text x="70" y="88" text-anchor="middle" font-size="52" fill="#fff"><tspan font-size="32" dy="-10">$</tspan><tspan dy="10">8</tspan></text>
  </svg>

  <footer>
    <h3 class="hours-title">BUSINESS HOURS</h3>
    <p class="hours-note">WEATHER MAY AFFECT THESE HOURS</p>
    <p class="hours-list">MONDAY-SATURDAY<br>8:00 AM-6:00 PM<br>SUNDAY 8:00 AM-5:00 PM</p>
  </footer>

  <section class="extras">
    <h3 class="extras-title">EXTRAS</h3>
    <p class="extras-items">Bug Treatment &nbsp;•&nbsp; Hot Wax Treatment &nbsp;•&nbsp; Tire Shine</p>
  </section>
</main>
</body>
</html>
```